Copper Ridge Upkeep and Errand Flyer

We need a flyer for copper ridge upkeep and errand service. We specialize in and provide residential maintenance and errand services to retired and semi retired persons living in the Lake Norman area. The services we include:
Lighting and plumbing repairs
Ceiling fan installation
Handicap accessories
Locks and security
Picture hanging
Hang blinds
Furniture arrangement / assembly
Pressure washing
Battery Jump start
and more...

Our Concierge services include:
Errand running
Grocery shopping
Wellness Checks
Dog Walk
Garbage Collection
and more...

We offer monthly service agreements and 24/7 access
Call text or e-mail for more information
555.418.2963
1copperridgeupk@quillbox-mail.net

The design should invoke a sense of trust and a customer service driven mission

Target Market(s)

Residential maintenance

Industry/Entity Type

Property Maintenance

Contact Information for Business Card

Dale Hurst
20814 Fennick Gale Rd.
Cornelius NC 28947
555.418.2963
with uploaded logo

Requirements
Nice to have
• Would like a postcard size flyer. Front and back
Should not have
• No pics of of people wearing hard hats or pics of blueprints. No pics of commercial or industrial maintenance.

```html
<!DOCTYPE html>
<html lang="en">
<head>
<meta charset="utf-8">
<title>Copper Ridge Upkeep and Errand – Flyer and Business Card</title>
<link rel="stylesheet" href="https://fonts.googleapis.com/css2?family=Oswald:wght@700&family=Questrial&family=Montserrat:ital,wght@1,700&display=swap">
<style>
  :root{
    --page:#e9e7e4;
    --ink-dark:#252324;
    --ink-mid:#3b393b;
    --panel-grey:#4a484b;
    --silver:#c9c9cc;
    --banner:#d9d9db;
    --red:#d3202a;
    --white:#ffffff;
    --text-light:#f2f2f2;
    --logo-grey:#5a5a5c;
  }
  *{box-sizing:border-box;margin:0;padding:0}
  html,body{width:1200px;height:1200px;overflow:hidden;background:var(--page)}
  body{position:relative;font-family:"Questrial",Arial,sans-serif}

  .flyer{position:absolute;top:40px;width:540px;height:700px;overflow:hidden;background:var(--ink-dark);box-shadow:0 4px 14px rgba(0,0,0,.18)}
  .flyer--front{left:40px}
  .flyer--back{left:620px}
  .flyer__art{position:absolute;inset:0;width:100%;height:100%}

  .brand{position:absolute;display:flex;align-items:center;gap:10px}
  .brand__dot{width:34px;height:34px;border-radius:50%;background:var(--red);flex:none}
  .brand__name{font-family:"Questrial",Arial,sans-serif;color:var(--logo-grey);font-size:19px;line-height:1.1}
  .flyer--front .brand{left:26px;top:62px}
  .flyer--back .brand{right:22px;top:36px}

  .section-title{position:absolute;background:var(--banner);padding:6px 16px 4px 12px;clip-path:polygon(0 0,100% 0,97% 100%,0 100%);
    font-family:"Oswald",Impact,sans-serif;font-weight:700;color:var(--red);font-size:23px;letter-spacing:.2px;text-transform:uppercase}
  .flyer--front .section-title{left:30px;top:246px}
  .flyer--back .section-title{left:0;top:344px;padding-left:8px}

  .service-list{position:absolute;list-style:none;color:var(--text-light);font-size:19px}
  .service-list li{position:relative;padding-left:22px;height:29px;line-height:29px}
  .service-list li::before{content:"";position:absolute;left:2px;top:9px;width:10px;height:13px;background:var(--red);
    clip-path:polygon(0 0,45% 0,100% 50%,45% 100%,0 100%,55% 50%)}
  .flyer--front .service-list{left:36px;top:290px}
  .flyer--back .service-list{left:10px;top:388px}

  .offer{position:absolute;left:10px;top:548px;width:330px;font-family:"Montserrat",Arial,sans-serif;font-style:italic;font-weight:700;
    color:var(--text-light);font-size:19px;line-height:26px;text-transform:uppercase}
  .contact-phone{position:absolute;left:12px;top:632px;color:var(--white);font-family:"Montserrat",Arial,sans-serif;font-weight:700;font-size:26px}
  .contact-email{position:absolute;left:12px;top:668px;color:var(--white);font-size:13px}

  .card{position:absolute;top:800px;width:500px;height:286px;overflow:hidden;box-shadow:0 4px 14px rgba(0,0,0,.2)}
  .card--back{left:40px;background:linear-gradient(135deg,#4a484b,#2f2d2f)}
  .card--front{left:660px;background:var(--white)}
  .card__art{position:absolute;inset:0;width:100%;height:100%}
  .card--back .brand{left:150px;top:122px}
  .card--back .brand__name{color:var(--silver)}
  .card__tab{position:absolute;right:-10px;top:30px;background:var(--red);color:var(--white);font-size:18px;padding:8px 26px 8px 22px;border-radius:18px 0 0 18px}
  .card--front .brand{left:26px;top:58px}
  .card__name{position:absolute;right:28px;top:52px;text-align:right;color:var(--ink-mid)}
  .card__name strong{display:block;font-weight:400;font-size:24px}
  .card__name span{display:block;font-size:11px;letter-spacing:.5px}
  .card__contact{position:absolute;display:flex;align-items:center;gap:8px;color:var(--text-light);font-size:11.5px}
  .card__contact svg{width:20px;height:20px;flex:none}
</style>
</head>
<body>

<section class="flyer flyer--front" aria-label="Flyer front">
  <svg class="flyer__art" viewBox="0 0 540 700" aria-hidden="false">
    <defs>
      <linearGradient id="frontBg" x1="0" y1="0" x2="1" y2="1">
        <stop offset="0" stop-color="#2a2829"/><stop offset=".55" stop-color="#3a383c"/><stop offset="1" stop-color="#262426"/>
      </linearGradient>
      <linearGradient id="bellTones" x1="0" y1="0" x2="1" y2="1">
        <stop offset="0" stop-color="#e6d6c8"/><stop offset=".5" stop-color="#9a9590"/><stop offset="1" stop-color="#4a3f38"/>
      </linearGradient>
      <linearGradient id="coneTones" x1="0" y1="0" x2="1" y2="1">
        <stop offset="0" stop-color="#4c4a52" stop-opacity=".2"/><stop offset=".6" stop-color="#9a5a3a" stop-opacity=".75"/><stop offset="1" stop-color="#3a2e2a"/>
      </linearGradient>
      <linearGradient id="worksiteTones" x1="0" y1="0" x2="1" y2="1">
        <stop offset="0" stop-color="#8b8a86"/><stop offset=".5" stop-color="#6a6a66"/><stop offset="1" stop-color="#c9b53a"/>
      </linearGradient>
    </defs>
    <rect width="540" height="700" fill="url(#frontBg)"/>
    <polygon points="0,0 330,0 165,165 0,165" fill="#ffffff"/>
    <polygon points="300,700 540,470 540,700" fill="url(#coneTones)" role="img" aria-label="Photo of stacked orange safety cones"/>
    <polygon points="330,0 540,0 540,330 165,165" fill="url(#bellTones)" role="img" aria-label="Photo of a hand pressing a silver service bell"/>
    <polyline points="330,0 165,165 540,330" fill="none" stroke="#d4d4d8" stroke-width="4"/>
    <polygon points="0,555 360,700 0,700" fill="url(#worksiteTones)" role="img" aria-label="Photo of a small excavator and traffic cones on a roadwork site"/>
    <line x1="0" y1="555" x2="360" y2="700" stroke="#d4d4d8" stroke-width="4"/>
  </svg>

  <div class="brand"><span class="brand__dot"></span><span class="brand__name">Copper Ridge<br>Upkeep &amp; Errand</span></div>

  <h2 class="section-title">The services we include:</h2>
  <ul class="service-list">
    <li>Lighting and plumbing repairs</li>
    <li>Ceiling fan installation</li>
    <li>Handicap accessories</li>
    <li>Locks and security</li>
    <li>Picture hanging</li>
    <li>Hang blinds</li>
    <li>Furniture arrangement / assembly</li>
    <li>Pressure washing</li>
    <li>Battery Jump start and more...</li>
  </ul>
</section>

<section class="flyer flyer--back" aria-label="Flyer back">
  <svg class="flyer__art" viewBox="0 0 540 700">
    <defs>
      <linearGradient id="backBg" x1="0" y1="0" x2="1" y2="1">
        <stop offset="0" stop-color="#2a2829"/><stop offset=".6" stop-color="#48464b"/><stop offset="1" stop-color="#2a2829"/>
      </linearGradient>
      <linearGradient id="plumbTones" x1="0" y1="0" x2="1" y2="1">
        <stop offset="0" stop-color="#3c3a3c"/><stop offset=".5" stop-color="#8f8c8a"/><stop offset="1" stop-color="#d8d4d0"/>
      </linearGradient>
      <radialGradient id="bellFaint" cx=".5" cy=".5" r=".5">
        <stop offset="0" stop-color="#9b9aa0" stop-opacity=".7"/><stop offset="1" stop-color="#48464b" stop-opacity="0"/>
      </radialGradient>
      <linearGradient id="truckTones" x1="0" y1="0" x2="1" y2="1">
        <stop offset="0" stop-color="#cfd3d6"/><stop offset=".5" stop-color="#7d8a6e"/><stop offset="1" stop-color="#3b5fa8"/>
      </linearGradient>
    </defs>
    <rect width="540" height="700" fill="url(#backBg)"/>
    <polygon points="180,0 540,0 540,145 360,145" fill="#ffffff"/>
    <ellipse cx="450" cy="400" rx="140" ry="130" fill="url(#bellFaint)" role="img" aria-label="Faded photo of a hand above a service bell"/>
    <polygon points="0,0 180,0 360,145 0,330" fill="url(#plumbTones)" role="img" aria-label="Photo of a repairman fixing a kitchen faucet"/>
    <polyline points="180,0 360,145 0,330" fill="none" stroke="#d4d4d8" stroke-width="4"/>
    <polygon points="0,540 360,520 300,640 0,650" fill="#5a585c" opacity=".8"/>
    <polygon points="540,480 540,700 420,700 290,650" fill="url(#truckTones)" role="img" aria-label="Photo of collection trucks along a country road"/>
    <polyline points="540,480 290,650 420,700" fill="none" stroke="#d4d4d8" stroke-width="4"/>
  </svg>

  <div class="brand"><span class="brand__dot"></span><span class="brand__name">Copper Ridge<br>Upkeep &amp; Errand</span></div>

  <h2 class="section-title">Our concierge services include:</h2>
  <ul class="service-list">
    <li>Errand running</li>
    <li>Grocery shopping</li>
    <li>Wellness Checks</li>
    <li>Dog Walk</li>
    <li>Garbage Collection and more...</li>
  </ul>

  <p class="offer">We offer monthly service agreements and 24/7 access</p>
  <p class="contact-phone">555.418.2963</p>
  <p class="contact-email">1copperridgeupk@quillbox-mail.net</p>
</section>

<section class="card card--back" aria-label="Business card back">
  <div class="card__tab">555.418.2963</div>
  <div class="brand"><span class="brand__dot"></span><span class="brand__name">Copper Ridge<br>Upkeep &amp; Errand</span></div>
</section>

<section class="card card--front" aria-label="Business card front">
  <svg class="card__art" viewBox="0 0 500 286">
    <path d="M0,230 L40,230 L20,286 L0,286 Z" fill="#bdbdc0"/>
    <path d="M105,200 Q112,163 140,162 L500,136 L500,152 L138,178 Q118,180 112,202 Z" fill="var(--red)"/>
    <path d="M70,286 L105,200 Q112,180 138,178 L500,152 L500,286 Z" fill="#2f2d2f"/>
  </svg>
  <div class="brand"><span class="brand__dot"></span><span class="brand__name">Copper Ridge<br>Upkeep &amp; Errand</span></div>
  <div class="card__name"><strong>NAME GOSE HERE</strong><span>TITLE GOSE HERE</span></div>

  <div class="card__contact" style="left:122px;top:202px">
    <svg viewBox="0 0 20 20"><circle cx="10" cy="10" r="10" fill="#ddd"/><path d="M6.5 5 L8.5 5 L9.3 7.6 L8 8.6 Q9.2 11 11.4 12 L12.4 10.7 L15 11.5 L15 13.5 Q9 14.5 6 7.5 Z" fill="#2f2d2f"/></svg>
    555.418.2963
  </div>
  <div class="card__contact" style="left:122px;top:244px">
    <svg viewBox="0 0 20 20"><circle cx="10" cy="10" r="10" fill="#ddd"/><rect x="5" y="6.5" width="10" height="7" fill="#2f2d2f"/><path d="M5 6.5 L10 10.5 L15 6.5" fill="none" stroke="#ddd" stroke-width="1"/></svg>
    1copperridgeupk@quillbox-mail.net
  </div>
  <div class="card__contact" style="left:330px;top:184px">
    <svg viewBox="0 0 20 20"><circle cx="10" cy="10" r="10" fill="#ddd"/><path d="M10 4 Q14 4 14 8 Q14 11 10 16 Q6 11 6 8 Q6 4 10 4 Z" fill="#2f2d2f"/><circle cx="10" cy="8" r="1.6" fill="#ddd"/></svg>
    Adress line, Street name
  </div>
  <div class="card__contact" style="left:330px;top:224px">
    <svg viewBox="0 0 20 20"><circle cx="10" cy="10" r="10" fill="#ddd"/><circle cx="10" cy="10" r="5.5" fill="none" stroke="#2f2d2f" stroke-width="1.2"/><ellipse cx="10" cy="10" rx="2.4" ry="5.5" fill="none" stroke="#2f2d2f" stroke-width="1"/><line x1="4.5" y1="10" x2="15.5" y2="10" stroke="#2f2d2f" stroke-width="1"/></svg>
    www.copperridge-upkeep.net
  </div>
</section>

</body>
</html>
```